Millennial Survey Statistics Infogrpahic

We're a boutique creative consultancy specializing in informing Baby Boomers and Genreation X on how the millennial generation works, votes, and buys.

We recently conducted a survey amongst the millennial generation and we need to represent these stats in an infographic, that's visually interesting as well as concisely getting our information across to Boomers and Xer's.

We would like to see infographic designs that are split into three sections WORK, VOTE, and BUY with each section displaying its corresponding stats. We would also like to see designs that use our existing assets and style guide (Attached), as well as creating new assets as needed.

The Final design should communicate the stats in a visually appealing way to our target audience of baby boomers and generation x.

Target Market(s)

Generation X and Baby Boomers

Industry/Entity Type

Boutique

Requirements
Must have
• Use of our Style Guide approved colors, and fonts.

```html
<!DOCTYPE html>
<html lang="en">
<head>
<meta charset="utf-8">
<title>Vote – Millennial Survey Statistics</title>
<link rel="stylesheet" href="https://fonts.googleapis.com/css2?family=Arimo:wght@400;700&display=swap">
<style>
  :root {
    --poster-bg: #e4e4e4;
    --green-title: #8db77a;
    --green-text: #79a866;
    --green-1: #5c9b47;
    --green-2: #80b36b;
    --green-3: #4e8e3d;
    --green-4: #6ea85a;
    --line: #b9b9b9;
    --white: #ffffff;
  }
  * { margin: 0; padding: 0; box-sizing: border-box; }
  html, body { width: 1200px; height: 1000px; overflow: hidden; }
  body {
    background: var(--poster-bg);
    font-family: "Arimo", Arial, sans-serif;
    position: relative;
  }
  .section-title {
    position: absolute; left: 44px; top: 14px;
    font-size: 96px; font-weight: 700; letter-spacing: -2px;
    color: var(--green-title);
  }
  .charts { position: absolute; inset: 0; }
  .seg-label {
    font-size: 12px; font-weight: 700; fill: var(--white);
    text-anchor: middle; dominant-baseline: central;
  }
  .chart-name {
    position: absolute; width: 110px; text-align: center;
    transform: translate(-50%, -50%);
    font-size: 17px; font-weight: 700; line-height: 1.12;
    color: var(--green-title);
  }
  .chart-name.small { font-size: 14px; }
  .callout {
    position: absolute; font-size: 10px; line-height: 1.18;
    color: var(--green-text); max-width: 190px;
  }
  .callout strong { display: block; font-weight: 700; }
  .callout p + p { margin-top: 8px; }
</style>
</head>
<body>
  <h1 class="section-title">VOTE</h1>

  <svg class="charts" width="1200" height="1000" viewBox="0 0 1200 1000">
    <defs>
      <filter id="soft-shadow" x="-30%" y="-30%" width="160%" height="160%">
        <feDropShadow dx="0" dy="3" stdDeviation="4" flood-color="#000" flood-opacity="0.3"/>
      </filter>
      <radialGradient id="hub" cx="50%" cy="40%" r="60%">
        <stop offset="0" stop-color="#ffffff"/>
        <stop offset="1" stop-color="#e6e6e6"/>
      </radialGradient>
    </defs>

    <g fill="none" stroke="var(--line)" stroke-width="1">
      <polyline points="140,316 140,264 238,264"/>
      <polyline points="473,316 473,264 560,264"/>
      <polyline points="871,301 871,252 970,252"/>
      <polyline points="270,721 270,660 370,660"/>
      <polyline points="698,728 698,652 795,652"/>
    </g>
    <g fill="var(--white)" stroke="var(--green-1)" stroke-width="3">
      <circle cx="242" cy="264" r="4"/>
      <circle cx="564" cy="264" r="4"/>
      <circle cx="974" cy="252" r="4"/>
      <circle cx="374" cy="660" r="4"/>
      <circle cx="799" cy="652" r="4"/>
    </g>

    <g class="donut" transform="translate(140 416)">
      <g transform="rotate(-90)" fill="none" stroke-width="38" filter="url(#soft-shadow)">
        <circle r="82" pathLength="98" stroke="var(--green-2)" stroke-dasharray="30 98" stroke-dashoffset="0"/>
        <circle r="82" pathLength="98" stroke="var(--green-1)" stroke-dasharray="25 98" stroke-dashoffset="-30"/>
        <circle r="82" pathLength="98" stroke="var(--green-3)" stroke-dasharray="19 98" stroke-dashoffset="-55"/>
        <circle r="82" pathLength="98" stroke="var(--green-4)" stroke-dasharray="5 98" stroke-dashoffset="-74"/>
        <circle r="82" pathLength="98" stroke="var(--green-1)" stroke-dasharray="7 98" stroke-dashoffset="-79"/>
        <circle r="82" pathLength="98" stroke="var(--green-3)" stroke-dasharray="12 98" stroke-dashoffset="-86"/>
      </g>
      <circle r="62" fill="url(#hub)" filter="url(#soft-shadow)"/>
    </g>
    <text class="seg-label" x="207" y="369">30 %</text>
    <text class="seg-label" x="173" y="491">25%</text>
    <text class="seg-label" x="71" y="461">19 %</text>
    <text class="seg-label" x="59" y="402">5 %</text>
    <text class="seg-label" x="71" y="371">7 %</text>
    <text class="seg-label" x="109" y="340">12 %</text>

    <g class="donut" transform="translate(473 416)">
      <g transform="rotate(-90)" fill="none" stroke-width="38" filter="url(#soft-shadow)">
        <circle r="82" pathLength="100" stroke="var(--green-2)" stroke-dasharray="69 100" stroke-dashoffset="0"/>
        <circle r="82" pathLength="100" stroke="var(--green-3)" stroke-dasharray="10 100" stroke-dashoffset="-69"/>
        <circle r="82" pathLength="100" stroke="var(--green-1)" stroke-dasharray="21 100" stroke-dashoffset="-79"/>
      </g>
      <circle r="62" fill="url(#hub)" filter="url(#soft-shadow)"/>
    </g>
    <text class="seg-label" x="541" y="462">69 %</text>
    <text class="seg-label" x="393" y="410">10 %</text>
    <text class="seg-label" x="422" y="351">21 %</text>

    <g class="donut" transform="translate(871 401)">
      <g transform="rotate(-90)" fill="none" stroke-width="38" filter="url(#soft-shadow)">
        <circle r="82" pathLength="100" stroke="var(--green-1)" stroke-dasharray="20 100" stroke-dashoffset="0"/>
        <circle r="82" pathLength="100" stroke="var(--green-2)" stroke-dasharray="20 100" stroke-dashoffset="-20"/>
        <circle r="82" pathLength="100" stroke="var(--green-4)" stroke-dasharray="20 100" stroke-dashoffset="-40"/>
        <circle r="82" pathLength="100" stroke="var(--green-3)" stroke-dasharray="20 100" stroke-dashoffset="-60"/>
        <circle r="82" pathLength="100" stroke="var(--green-2)" stroke-dasharray="20 100" stroke-dashoffset="-80"/>
      </g>
      <circle r="62" fill="url(#hub)" filter="url(#soft-shadow)"/>
    </g>
    <text class="seg-label" x="919" y="335">20%</text>
    <text class="seg-label" x="949" y="426">20%</text>
    <text class="seg-label" x="871" y="483">20%</text>
    <text class="seg-label" x="793" y="426">20%</text>
    <text class="seg-label" x="823" y="335">20%</text>

    <g class="donut" transform="translate(270 821)">
      <g transform="rotate(-90)" fill="none" stroke-width="38" filter="url(#soft-shadow)">
        <circle r="82" pathLength="210" stroke="var(--green-2)" stroke-dasharray="74 210" stroke-dashoffset="0"/>
        <circle r="82" pathLength="210" stroke="var(--green-3)" stroke-dasharray="70 210" stroke-dashoffset="-74"/>
        <circle r="82" pathLength="210" stroke="var(--green-4)" stroke-dasharray="66 210" stroke-dashoffset="-144"/>
      </g>
      <circle r="62" fill="url(#hub)" filter="url(#soft-shadow)"/>
    </g>
    <text class="seg-label" x="343" y="784">74 %</text>
    <text class="seg-label" x="260" y="902">70 %</text>
    <text class="seg-label" x="201" y="776">66 %</text>

    <g class="donut" transform="translate(698 828)">
      <g transform="rotate(-90)" fill="none" stroke-width="38" filter="url(#soft-shadow)">
        <circle r="82" pathLength="200" stroke="var(--green-1)" stroke-dasharray="70 200" stroke-dashoffset="0"/>
        <circle r="82" pathLength="200" stroke="var(--green-2)" stroke-dasharray="59 200" stroke-dashoffset="-70"/>
        <circle r="82" pathLength="200" stroke="var(--green-3)" stroke-dasharray="41 200" stroke-dashoffset="-129"/>
        <circle r="82" pathLength="200" stroke="var(--green-4)" stroke-dasharray="30 200" stroke-dashoffset="-170"/>
      </g>
      <circle r="62" fill="url(#hub)" filter="url(#soft-shadow)"/>
    </g>
    <text class="seg-label" x="771" y="791">70 %</text>
    <text class="seg-label" x="699" y="910">59%</text>
    <text class="seg-label" x="618" y="829">41 %</text>
    <text class="seg-label" x="661" y="755">30%</text>
  </svg>

  <div class="chart-name" style="left:140px; top:416px;">POLITICAL PARTY</div>
  <div class="chart-name" style="left:473px; top:416px;">VOTING</div>
  <div class="chart-name" style="left:871px; top:401px;">“HEAR or LEARN” ABOUT POLITICS</div>
  <div class="chart-name" style="left:270px; top:821px;">APPROVAL ON SOCIAL ISSUES</div>
  <div class="chart-name small" style="left:698px; top:828px;">MILLENNIALS BELIEVE THEIR GENERATION IS…</div>

  <div class="callout" style="left:262px; top:204px;">
    <strong>Political Party</strong>
    Democratic 30%<br>Republican 25%<br>Independent 19%<br>Libertarian 5%<br>Don't Care 12%<br>Declined to state 7%
  </div>
  <div class="callout" style="left:584px; top:204px; max-width:170px;">
    <p><strong>VOTING</strong>69% of Millennials are registered to vote</p>
    <p>10% plan to register to vote in “the near future”</p>
    <p>21% claimed “politics is generally not my thing.”</p>
  </div>
  <div class="callout" style="left:994px; top:204px; max-width:200px;">
    <strong>TOP 5 PLACES MILLENNIALS “HEAR or LEARN” ABOUT POLITICS</strong>
    Television<br>Social Media (Chirper, FriendBook, etc.)<br>Newspapers/Online new sources<br>Radio<br>Blogs
  </div>
  <div class="callout" style="left:394px; top:642px;">
    <strong>APPROVAL ON SOCIAL ISSUES</strong>
    Marriage Equality 74%<br>Woman's Right to Abortion 70%<br>Legalized Marijuana 66%
  </div>
  <div class="callout" style="left:819px; top:620px; max-width:180px;">
    <strong>MILLENNIALS BELIEVE THEIR GENERATION IS…</strong>
    Politically Apathetic 70%<br>Politically Engaged 30%<br>Optimistic about America's Future 41%<br>Not Optimistic…America's Future 59%
  </div>
</body>
</html>
```